Young Accounting firm needing a captivating business card

We need a business card design that forces the person to look at the card because its either gold foil, plastic, or lettering pop up etc. We already have a logo with a specific gold color and we need to make it pop. We are an accounting firm. I need the words" accounting, payroll, licenses, audits, taxes" somewhere on the business card so as to describe what we do- preferably on the side where the logo is at.

Industry/Entity Type

Accounting

Contact Information for Business Card

Address 48207 9th Ave N Ste 305, Cedar Hollow, WA 98421
Business Phone (360)418-2967
Fax (360)418-2051
Office Cell Phone (360)506-7139

Font styles to use
Serif

Colors
85abd2

Requirements
Must have
• It should state
• "Accounting" "Taxes" "Audits" "Licenses" "Payroll"
Nice to have
• Matte with gold foil, different textures, With Either a textured ivory background or gray blue slate background
Should not have
• colorful colors

```html
<!DOCTYPE html>
<html lang="en">
<head>
<meta charset="utf-8">
<title>Ledgerline Business Card</title>
<link rel="stylesheet" href="https://fonts.googleapis.com/css2?family=Montserrat:wght@400;500;700&display=swap">
<style>
  :root {
    --backdrop: #c9ccd0;
    --card: #2a2928;
    --gold: #c9962e;
    --gold-light: #e7d3a1;
    --cream: #efe6cf;
  }
  * { box-sizing: border-box; margin: 0; padding: 0; }
  html, body { width: 1200px; height: 800px; overflow: hidden; }
  body {
    background: linear-gradient(135deg, #b9bcc0 0%, var(--backdrop) 55%, #dde2e6 100%);
    font-family: "Montserrat", sans-serif;
    position: relative;
  }
  .card {
    position: absolute;
    left: 320px;
    width: 560px;
    height: 320px;
    background: var(--card);
    box-shadow: 0 6px 18px rgba(0,0,0,0.25);
  }
  .card--front { top: 60px; }
  .card--back { top: 420px; }

  /* Front */
  .front-brand {
    position: absolute;
    top: 110px; left: 0; right: 0;
    display: flex; align-items: center; justify-content: center; gap: 14px;
  }
  .brand-mark {
    width: 34px; height: 34px;
    background: var(--gold);
  }
  .brand-name {
    font-size: 40px;
    font-weight: 500;
    color: var(--gold);
    letter-spacing: 0.5px;
  }
  .front-services {
    position: absolute;
    top: 212px; left: 0; right: 0;
    text-align: center;
    font-size: 13px;
    color: var(--gold);
    letter-spacing: 0.6px;
  }
  .front-services .lead { color: var(--gold-light); }

  /* Back */
  .back-brand {
    position: absolute;
    left: 0; top: 0; width: 250px; height: 320px;
    display: flex; flex-direction: column; align-items: center; justify-content: center; gap: 16px;
  }
  .back-brand .brand-mark { width: 90px; height: 90px; background: var(--gold-light); }
  .back-brand .brand-name { font-size: 30px; color: var(--gold-light); }
  .divider {
    position: absolute;
    left: 262px; top: 50px;
    width: 2px; height: 220px;
    background: var(--gold);
  }
  .contact {
    position: absolute;
    left: 292px; top: 58px;
    color: var(--gold);
  }
  .contact-name {
    font-size: 19px; font-weight: 700;
    color: var(--cream);
    letter-spacing: 0.8px;
  }
  .contact-title {
    font-size: 14px;
    color: var(--cream);
    margin-bottom: 18px;
  }
  .contact-address { font-size: 15px; line-height: 20px; margin-bottom: 6px; }
  .contact-list { list-style: none; font-size: 15px; line-height: 21px; }
  .contact-list li { display: flex; align-items: center; gap: 8px; }
  .contact-list svg { width: 13px; height: 13px; fill: none; stroke: var(--gold); stroke-width: 1.6; flex: none; }
</style>
</head>
<body>
  <section class="card card--front">
    <div class="front-brand">
      <span class="brand-mark"></span>
      <span class="brand-name">Ledgerline</span>
    </div>
    <p class="front-services"><span class="lead">Accounting</span> | Licenses | Audits | Taxes | Payroll</p>
  </section>

  <section class="card card--back">
    <div class="back-brand">
      <span class="brand-mark"></span>
      <span class="brand-name">Ledgerline</span>
    </div>
    <div class="divider"></div>
    <div class="contact">
      <p class="contact-name">Daniel Harper</p>
      <p class="contact-title">President</p>
      <p class="contact-address">48207 9th Ave N Ste 305<br>Cedar Hollow, WA 98421</p>
      <ul class="contact-list">
        <li><svg viewBox="0 0 16 16"><path d="M3 2l3 1 1 3-2 1a8 8 0 0 0 4 4l1-2 3 1 1 3-2 1C7 14 2 9 2 4z"/></svg>(360) 418-2967</li>
        <li><svg viewBox="0 0 16 16"><rect x="4" y="1.5" width="8" height="13" rx="1.5"/><path d="M7 12h2"/></svg>(360) 506-7139</li>
        <li><svg viewBox="0 0 16 16"><rect x="2" y="6" width="12" height="7" rx="1"/><path d="M4 6V2h8v4M5 10h6"/></svg>(360) 418-2051</li>
        <li><svg viewBox="0 0 16 16"><rect x="1.5" y="3.5" width="13" height="9"/><path d="M1.5 3.5L8 9l6.5-5.5"/></svg>daniel@ledgerlinetax.com</li>
        <li><svg viewBox="0 0 16 16"><circle cx="8" cy="8" r="6.5"/><path d="M1.5 8h13M8 1.5c-3 3.5-3 9.5 0 13M8 1.5c3 3.5 3 9.5 0 13"/></svg>www.ledgerlinetax.com</li>
      </ul>
    </div>
  </section>
</body>
</html>
```